Animal Hospital Business Cards

Make a business card look like the attached example

*Use the same blue/black coloring
*Brisket Hollow Animal Hospital (instead of pet home rounds)
*Emergency Services (instead of tamsin creek clinic)
*House Calls (instead of open 7 days by appointment)
*Change address to 278 Brisket Hollow Rd Fernmoor, VT 05899
*Open 7 days a week (instead of emergency service)
*Add the website www.briskethollowanimalhospital.example

On the back...
*instead of the text outlined in red, just white
*instead of the light blue, try your best to make it just like the blue and black on the front side of the card
*Delete "designed and printed by 9 whiskers inc, www.pressfeline.example

Requirements
Must have
• look just like the attached example with requested edits/changes

```html
<!DOCTYPE html>
<html lang="en">
<head>
<meta charset="utf-8">
<title>Brisket Hollow Animal Hospital – Business Card</title>
<link href="https://fonts.googleapis.com/css2?family=Roboto:wght@400;700;900&family=Tinos:wght@400;700&display=swap" rel="stylesheet">
<style>
  :root {
    --blue-dark: #0a6fa8;
    --blue: #1593cf;
    --blue-light: #2fb0e6;
    --ink: #111111;
    --red: #e0242b;
    --stripe: #c9cccf;
    --paper: #ffffff;
    --paper-shade: #eceeef;
    --page: #e9e6e1;
    --mon: #a2356c; --tue: #e36a1c; --wed: #4b86b0; --thu: #e2202a;
    --fri: #e9df1c; --sat: #e35a8e; --sun: #1f8a3a;
  }
  * { box-sizing: border-box; margin: 0; padding: 0; }
  html, body { width: 1200px; height: 780px; overflow: hidden; }
  body {
    background: var(--page);
    font-family: "Roboto", Arial, sans-serif;
    color: var(--ink);
    display: flex; flex-direction: column; align-items: center; justify-content: center; gap: 18px;
  }
  .card {
    width: 620px; height: 354px; border-radius: 18px; overflow: hidden;
    background: linear-gradient(180deg, var(--paper) 0%, var(--paper-shade) 100%);
    box-shadow: 0 4px 14px rgba(0,0,0,.18);
    position: relative; display: flex; flex-direction: column;
  }
  .band {
    background: linear-gradient(180deg, var(--blue-light) 0%, var(--blue) 45%, var(--blue-dark) 100%);
    color: #fff; text-align: center; font-weight: 700;
  }
  .stripe { height: 9px; background: var(--stripe); flex: none; }
  /* front */
  .front .band-top { height: 64px; font-size: 33px; line-height: 64px; }
  .front .band-bottom { height: 62px; font-size: 32px; line-height: 62px; }
  .front .body { flex: 1; display: grid; grid-template-columns: 150px 1fr 150px; align-items: center; padding: 0 16px; }
  .side-title { font-size: 23px; font-weight: 700; line-height: 1.05; }
  .side-sub { font-size: 11px; font-weight: 700; margin-top: 3px; }
  .address { font-size: 13px; font-weight: 700; line-height: 1.25; margin-top: 16px; }
  .left { align-self: end; padding-bottom: 22px; }
  .right { align-self: start; padding-top: 22px; text-align: center; }
  .years { font-size: 13px; font-weight: 700; margin-top: 18px; line-height: 1.2; }
  .center { text-align: center; }
  .doctor { font-family: "Tinos", "Times New Roman", serif; font-size: 25px; font-weight: 700; }
  .mark { display: inline-flex; align-items: center; gap: 7px; margin: 8px 0 6px; font-size: 15px; font-weight: 700; }
  .mark-dot { width: 16px; height: 16px; border-radius: 50%; border: 2px solid var(--red); }
  .species { font-family: "Tinos", "Times New Roman", serif; font-size: 17px; font-weight: 700; }
  .phone { color: var(--red); font-size: 27px; font-weight: 700; margin-top: 2px; }
  .web { font-size: 12px; margin-top: 2px; }
  /* back */
  .back .band-top { height: 96px; padding-top: 10px; flex: none; }
  .back .title { font-size: 30px; font-weight: 700; }
  .back .name { font-family: "Tinos", "Times New Roman", serif; font-size: 17px; font-weight: 700; margin-top: 2px; }
  .back .tel { font-size: 18px; font-weight: 700; margin-top: 1px; }
  .back .body { flex: 1; padding: 22px 28px 30px; display: flex; flex-direction: column; justify-content: space-between; }
  .line-row { display: flex; align-items: flex-end; gap: 6px; font-size: 17px; font-weight: 700; }
  .dots { flex: 1; border-bottom: 2px dotted var(--ink); margin-bottom: 5px; }
  .days { display: flex; justify-content: space-between; }
  .day {
    width: 66px; height: 48px; border-radius: 24px; color: #fff;
    font-size: 14px; font-weight: 700; display: flex; align-items: center; justify-content: center;
  }
  .day.mon { background: var(--mon); } .day.tue { background: var(--tue); }
  .day.wed { background: var(--wed); } .day.thu { background: var(--thu); }
  .day.fri { background: var(--fri); } .day.sat { background: var(--sat); }
  .day.sun { background: var(--sun); }
  .date-time { display: flex; gap: 30px; }
  .date-time .line-row { flex: 1; }
  .ampm { font-size: 12px; line-height: 1.1; font-weight: 700; }
</style>
</head>
<body>
  <section class="card front" aria-label="Front of business card">
    <div class="band band-top">Brisket Hollow Animal Hospital</div>
    <div class="stripe"></div>
    <div class="body">
      <div class="left">
        <div class="side-title">Emergency<br>Services</div>
        <div class="address">278 Brisket Hollow Rd<br>Fernmoor, VT 05899</div>
      </div>
      <div class="center">
        <div class="doctor">Rowan B. Keller, DVM</div>
        <div class="mark"><span class="mark-dot"></span>Brisket Hollow</div>
        <div class="species">• Cats • Dogs • Birds • Exotics</div>
        <div class="phone">(555) 301 - 0147</div>
        <div class="web">www.briskethollowanimalhospital.example</div>
      </div>
      <div class="right">
        <div class="side-title">House Calls</div>
        <div class="side-sub">By Appointment</div>
        <div class="years">30 Years<br>Of Experiance</div>
      </div>
    </div>
    <div class="stripe"></div>
    <div class="band band-bottom">Open 7 Days a Week</div>
  </section>

  <section class="card back" aria-label="Back of business card">
    <div class="band band-top">
      <div class="title">Veterinary Appointment</div>
      <div class="name">Rowan B. Keller, DVM</div>
      <div class="tel">(555) 301 - 0147</div>
    </div>
    <div class="stripe"></div>
    <div class="body">
      <div class="line-row">Your Appointment For <span class="dots"></span> Is On</div>
      <div class="days">
        <span class="day mon">Mon</span><span class="day tue">Tues</span><span class="day wed">Wed</span>
        <span class="day thu">Thur</span><span class="day fri">Fri</span><span class="day sat">Sat</span>
        <span class="day sun">Sun</span>
      </div>
      <div class="date-time">
        <div class="line-row">Date <span class="dots"></span></div>
        <div class="line-row">Time <span class="dots"></span> <span class="ampm">A.M<br>P.M</span></div>
      </div>
    </div>
  </section>
</body>
</html>
```